I need the following on my business card:
- Name: Dana Whitcomb
- License # 0M93216
- Title: Producer
- Phone: (555) 017-3904
- Email: Dana@CorbelInsuranceServices.com

- Company: Corbel Insurance Services
- Address: 27408 Larkmoor Ave Suite 610, Sherman Oaks, CA 90217
- Website: www.CorbelInsuranceServices.com

Also add our slogan on the card: "Where Trust Meets Coverage"

```html
<!DOCTYPE html>
<html lang="en">
<head>
<meta charset="utf-8">
<title>Corbel Insurance Services – Business Card</title>
<link href="https://fonts.googleapis.com/css2?family=Montserrat:wght@400;500;600&display=swap" rel="stylesheet">
<style>
  :root {
    --navy: #25337a;
    --green: #15994a;
    --white: #ffffff;
    --stage: #1c1c1e;
    --ink: #2b3576;
  }
  html, body {
    margin: 0;
    padding: 0;
    width: 1200px;
    height: 800px;
    overflow: hidden;
    background: var(--stage);
    font-family: "Montserrat", sans-serif;
  }
  .canvas {
    position: relative;
    width: 1200px;
    height: 800px;
  }
  .card {
    position: absolute;
    width: 550px;
    height: 314px;
    box-shadow: 0 8px 18px rgba(0,0,0,0.55);
    overflow: hidden;
  }
  /* Front */
  .card-front {
    left: 220px;
    top: 76px;
    background: var(--navy);
  }
  .front-wordmark {
    position: absolute;
    left: 0;
    right: 0;
    top: 140px;
    text-align: center;
    font-weight: 600;
  }
  .front-wordmark .name {
    display: block;
    font-size: 34px;
    letter-spacing: 0.5px;
    line-height: 1;
    color: var(--white);
  }
  .front-wordmark .sub {
    display: block;
    margin-top: 10px;
    font-size: 13px;
    letter-spacing: 4.6px;
    color: var(--green);
  }
  .slogan {
    position: absolute;
    left: 0;
    right: 0;
    top: 236px;
    margin: 0;
    text-align: center;
    color: var(--white);
    font-size: 13px;
    font-weight: 400;
    letter-spacing: 1px;
  }
  /* Back */
  .card-back {
    left: 430px;
    top: 408px;
    background: var(--white);
  }
  .name-band {
    position: absolute;
    left: 0;
    top: 38px;
    width: 272px;
    height: 35px;
    background: var(--navy);
    clip-path: polygon(0 0, 100% 0, 88% 100%, 0 100%);
  }
  .holder-name {
    position: absolute;
    left: 20px;
    top: 40px;
    margin: 0;
    font-size: 26px;
    font-weight: 500;
    color: var(--white);
    line-height: 32px;
    white-space: nowrap;
  }
  .holder-title {
    position: absolute;
    left: 19px;
    top: 76px;
    margin: 0;
    font-size: 14.5px;
    font-weight: 400;
    color: var(--ink);
  }
  .back-wordmark {
    position: absolute;
    right: 26px;
    top: 40px;
    text-align: center;
    font-weight: 600;
  }
  .back-wordmark .name {
    display: block;
    font-size: 24px;
    line-height: 1;
    letter-spacing: 0.3px;
    color: var(--navy);
  }
  .back-wordmark .sub {
    display: block;
    margin-top: 6px;
    font-size: 9.5px;
    letter-spacing: 2.6px;
    color: var(--green);
  }
  .contact-rule {
    position: absolute;
    left: 515px;
    top: 88px;
    width: 2px;
    bottom: 0;
    background: var(--green);
  }
  .contact-list {
    position: absolute;
    right: 52px;
    top: 154px;
    margin: 0;
    padding: 0;
    list-style: none;
    text-align: right;
    color: var(--ink);
    font-size: 14px;
    line-height: 22.5px;
    white-space: nowrap;
  }
  .contact-icon {
    position: absolute;
    left: 508px;
    width: 16px;
    height: 16px;
  }
  .icon-pin { top: 248px; }
  .icon-mail { top: 270px; }
</style>
</head>
<body>
<main class="canvas">
  <section class="card card-front" aria-label="Card front">
    <div class="front-wordmark">
      <span class="name">CORBEL</span>
      <span class="sub">INSURANCE SERVICES</span>
    </div>
    <p class="slogan">Where Trust Meets Coverage</p>
  </section>

  <section class="card card-back" aria-label="Card back">
    <div class="name-band"></div>
    <h1 class="holder-name">Dana Whitcomb</h1>
    <p class="holder-title">Producer</p>

    <div class="back-wordmark">
      <span class="name">CORBEL</span>
      <span class="sub">INSURANCE SERVICES</span>
    </div>

    <div class="contact-rule"></div>

    <ul class="contact-list">
      <li class="website">www.CorbelInsuranceServices.com</li>
      <li class="address">27408 Larkmoor Ave Suite 610</li>
      <li class="address">Sherman Oaks, CA 90217</li>
      <li class="license">L no: 0M93216</li>
      <li class="phone">(555) 017-3904</li>
      <li class="email">Dana@CorbelInsuranceServices.com</li>
    </ul>

    <svg class="contact-icon icon-pin" viewBox="0 0 16 16" aria-hidden="true">
      <circle cx="8" cy="8" r="8" fill="#15994a"/>
      <path d="M8 3.4a3 3 0 0 0-3 3c0 2.2 3 5.6 3 5.6s3-3.4 3-5.6a3 3 0 0 0-3-3z" fill="#fff"/>
      <circle cx="8" cy="6.4" r="1.2" fill="#15994a"/>
    </svg>
    <svg class="contact-icon icon-mail" viewBox="0 0 16 16" aria-hidden="true">
      <circle cx="8" cy="8" r="8" fill="#15994a"/>
      <rect x="3.8" y="5" width="8.4" height="6" rx="0.6" fill="#fff"/>
      <path d="M3.9 5.3 8 8.4l4.1-3.1" fill="none" stroke="#15994a" stroke-width="1"/>
    </svg>
  </section>
</main>
</body>
</html>
```